Personal Trainer website design

We are working with a personal trainer to design a website. They offer their primary services: Diet Coaching, In-Person Coaching (workouts), and Remote Coaching.
Some sites we like: https://www.mirabelfenn.com, https://kitarowe.com/en-us, https://bendwellstudio.co.uk
Thank you for taking the time to consider designing a website for us. We are web developers based in Stockton, CA USA. Most of our projects go through the same process. Understanding this process may help you win a project with us. We custom-code all of our websites in-house. We don’t have any requirements as to what tools you use for your design, but ask that you follow these guidelines.
IMAGES:
We ask that if you use any images, or icons in the design, have a link to the asset, so we can purchase the image/icon. Most of the designs we submit do not have the customer’s images on them unless they have some great images. Be creative; show us the feeling that you are trying to portray with your image choices. Use any royalty-free site you choose. We subscribe to Quillon and mostly use their images, but are ok to purchase images outside of Quillon.
FONTS:
We ask that you identify the fonts you’re using in the design. This can be done in a message if you want. We typically use Tembrik Fonts and Quillon Fonts.
CONTENT:
We're always open to different content and ideas. Often, we submit designs with stock images so that the client can see our vision. We typically go back and take pictures after the website launch to use their images with our vision. Lorem Ipsum is fine for paragraphs, but we ask that you make the Headers with correct English. We want to be able to show the vision and identify the sections of the website.
INSPIRATION:
We try and add a couple of links in the brief of some websites that we like to help you get started in your design.
REVISIONS:
We do not often ask for revisions of the designs unless we see something in the design that may not appeal to the client. If there are slight changes that we want to make, we simply do that in the development process.
FEEDBACK:
We rarely give feedback on designs during the design process. We are working on many website projects and do not have the time to give feedback. We usually respond if your request is well thought out and asks specific questions, but a note asking “feedback, please” usually goes unanswered.

```html
<!DOCTYPE html>
<html lang="en">
<head>
<meta charset="utf-8">
<title>Novafit — Personal Trainer</title>
<link href="https://fonts.googleapis.com/css2?family=Jost:wght@400;500;600&family=Sora:wght@600;700;800&display=swap" rel="stylesheet">
<style>
:root{
  --stage:#e4d3d6;
  --paper:#ffffff;
  --wine:#7a1623;
  --ink:#1d1b1b;
  --muted:#5d5757;
  --stone:#e5e1dd;
  --footer:#d9d5d0;
  --sage:#8aa43a;
}
*{box-sizing:border-box;margin:0;padding:0}
html,body{width:1200px;height:1200px;overflow:hidden;background:var(--stage);font-family:'Jost',sans-serif;color:var(--ink)}
.page{position:absolute;left:422px;top:69px;width:571px;height:1710px;background:var(--paper);transform:scale(0.6211);transform-origin:0 0;overflow:hidden}
.page > *{position:absolute}
.page p,.page span,.page li{line-height:1.45}
.logo{font-family:'Sora',sans-serif;font-weight:700;font-size:26px;color:var(--ink);letter-spacing:1px;display:flex;align-items:center;gap:6px}
.logo::after{content:"";width:12px;height:12px;border-radius:50%;background:var(--sage)}
.nav{left:76px;top:67px;display:flex;gap:7px;font-size:5px;font-weight:500;align-items:center}
.nav .pill{width:38px;height:15px}
.pill{background:var(--wine);color:#fff;border-radius:20px;font-size:5px;font-weight:500;display:flex;align-items:center;justify-content:center;white-space:nowrap}
.pill.grey{background:#dcd7d3;color:var(--ink)}
.eyebrow{font-size:6px;color:var(--ink);white-space:nowrap}
.h2{font-family:'Sora',sans-serif;font-weight:700;font-size:12px;color:var(--ink);white-space:nowrap}
.h2 b,.accent{color:var(--wine);font-weight:700}
.body{font-size:4.3px;color:var(--muted);line-height:1.6}
.photo{border-radius:2px}
.frame{border:1.5px solid var(--wine);border-radius:4px}
.stats{background:var(--wine);color:#fff;display:flex;justify-content:space-around;align-items:center;padding:0 6px}
.stats div{text-align:center;font-size:5.5px;line-height:1.4}
.stats strong{display:block;font-family:'Sora',sans-serif;font-size:10px;line-height:1.3;margin-bottom:1px}
.checks{left:76px;top:600px;font-size:4.5px;list-style:none}
.checks li{position:relative;padding-left:9px;height:10px}
.checks li::before{content:"";position:absolute;left:0;top:1px;width:4px;height:2px;border-left:1.2px solid var(--sage);border-bottom:1.2px solid var(--sage);transform:rotate(-45deg)}
.studio{left:76px;top:794px;width:419px;height:169px;background:linear-gradient(100deg,#8c1c2a 0%,#6d1320 45%,#a8313c 75%,#7a1623 100%);border-radius:3px}
.services{right:80px;top:888px;text-align:right;font-family:'Sora',sans-serif;font-weight:800;font-size:31px;line-height:35px;color:var(--wine);letter-spacing:-0.5px;white-space:nowrap}
.clip{left:0;top:0;width:571px;height:963px;overflow:hidden}
.clip .services{position:absolute;color:#fff}
.card{width:62px;height:62px;background:var(--stone);border-radius:3px;top:1120px}
.card svg{position:absolute;left:21px;top:9px}
.card p{position:absolute;left:4px;right:4px;top:36px;text-align:center;font-size:3.6px;color:var(--muted);line-height:1.5}
.press{left:148px;top:1220px;width:311px;height:54px;background:var(--stone);border-radius:3px;display:flex;justify-content:space-around;align-items:center;font-family:'Sora',sans-serif;font-weight:600;font-size:14px;color:#6f6a68}
.quote{top:1292px;height:85px;background:#f2efed;border-radius:2px}
.quote.fade{opacity:.4}
.avatar{width:54px;height:54px;border-radius:50%;background:radial-gradient(circle at 50% 40%,#cfc3bb,#8f8580)}
.qname{font-size:6px;font-weight:600;color:var(--wine)}
.qrole{font-size:4px;color:var(--muted)}
.stars{font-size:5px;color:var(--wine);letter-spacing:1px}
.arrow{font-size:14px;color:var(--wine);line-height:1}
.footer{left:0;top:1582px;width:571px;height:128px;background:var(--footer)}
.fhead{font-size:6.5px;font-weight:600;letter-spacing:.3px}
.flist{font-size:4.2px;line-height:9px;color:var(--ink)}
.flist span{display:block;line-height:9px}
.social{width:9px;height:9px;border-radius:50%;background:var(--ink)}
.payc{width:12px;height:7px;border-radius:1px;background:#bcb6b0;top:1675px}
</style>
</head>
<body>
<main class="page">

  <!-- hero -->
  <div class="logo" style="left:75px;top:14px">NOVAFIT</div>
  <nav class="nav">
    <span>ABOUT</span><span>SERVICES</span><span>THE JOURNAL</span><span>BLOG</span><span>SHOP</span><span>CONTACT</span>
    <span class="pill">MEMBERS</span>
  </nav>
  <div class="photo" role="img" aria-label="Trainer guiding a smiling client on a gym machine" style="left:285px;top:0;width:286px;height:239px;background:linear-gradient(135deg,#f1eeeb,#d9d3cd 60%,#b8aea6)"></div>
  <div style="left:479px;top:12px;width:14px;height:14px;border-radius:50%;background:var(--wine)">
    <svg width="14" height="14" viewBox="0 0 14 14" style="position:absolute;left:0;top:0"><circle cx="6.3" cy="6.3" r="2.4" fill="none" stroke="#fff" stroke-width="1"/><line x1="8" y1="8" x2="10" y2="10" stroke="#fff" stroke-width="1"/></svg>
  </div>
  <p class="eyebrow" style="left:77px;top:96px">Your personal workout and diet trainer</p>
  <h1 style="left:76px;top:110px;font-family:'Sora',sans-serif;font-weight:700;font-size:17.5px;line-height:19px;white-space:nowrap">A <span class="accent">healthy</span> outside<br>starts <span class="accent">from</span> the <span class="accent">inside.</span></h1>
  <p class="eyebrow" style="left:76px;top:156px">- Daniel Ashcombe</p>
  <p class="body" style="left:76px;top:172px;width:172px">Lorem ipsum dolor sit amet, consectetur adipiscing elit. Vestibulum vel fringilla mi. Integer eu sagittis quam, sit amet volutpat odio. Sed at tincidunt nisi. Integer eget felis quis nulla tincidunt commodo. Sed at tincidunt eros.</p>
  <div class="pill" style="left:76px;top:203px;width:46px;height:14px">GET STARTED</div>

  <!-- about -->
  <div class="frame" style="left:77px;top:298px;width:203px;height:186px"></div>
  <div class="photo" role="img" aria-label="Trainer and client reviewing a workout plan in the gym" style="left:85px;top:309px;width:187px;height:166px;background:linear-gradient(160deg,#9a9793,#c9c4bf 50%,#6e6a67)"></div>
  <p class="eyebrow" style="left:290px;top:304px">Our Mission, Vision, Passion and History</p>
  <h2 class="h2" style="left:290px;top:319px">About <b>Novafit</b></h2>
  <p class="body" style="left:290px;top:340px;width:202px">Curabitur tincidunt velit quam, eu condimentum ligula bibendum ac. Duis volutpat mauris eu lacinia lobortis. Nulla facilisi. In accumsan sed massa sit amet pellentesque. Mauris tristique, nunc pharetra vestibulum tempus, ex sem molestie neque, ac varius risus lacus sit amet purus. Cras laoreet dignis sim felis, ac congue augue. Donec blandit sem quis tortor hendrerit mattis. Mauris vitae ultricies libero. Curabitur suscipit dignissim augue, eleifend iaculis quam pellentesque eu. Suspendisse et eros fermentum, rhoncus nulla eu, pharetra sem. Sed pulvinar luctus sodales.</p>
  <div class="pill" style="left:290px;top:394px;width:45px;height:14px">GET STARTED</div>
  <div class="stats" style="left:290px;top:421px;width:208px;height:55px">
    <div><strong>100+</strong>On Demand<br>Classes</div>
    <div><strong>30+</strong>Live Stream<br>Classes</div>
    <div><strong>50+</strong>Private workout<br>classes</div>
  </div>
  <div style="left:502px;top:421px;width:69px;height:55px;background:var(--wine)"></div>

  <!-- why choose -->
  <p class="eyebrow" style="left:76px;top:542px">Our Facilities, Uniqueness And Features</p>
  <h2 class="h2" style="left:76px;top:556px">Why choose <b>Novafit</b></h2>
  <p class="body" style="left:76px;top:577px;width:170px">Curabitur tincidunt velit quam, eu condimentum ligula bibendum ac. Duis volutpat mauris eu lacinia lobortis.</p>
  <ul class="checks">
    <li>Lorem ipsum dolor sit amet</li>
    <li>Consectetur adipiscing elit</li>
    <li>Sed do eiusmod tempor incididunt</li>
    <li>Ut labore et dolore magna aliqua.</li>
    <li>Quis ipsum suspendisse ultrices gravida.</li>
  </ul>
  <div class="pill" style="left:76px;top:658px;width:45px;height:13px">GET STARTED</div>
  <div class="pill grey" style="left:128px;top:658px;width:44px;height:13px">BOOK NOW</div>
  <div class="frame" style="left:308px;top:526px;width:100px;height:60px;border-right:none;border-bottom:none"></div>
  <div class="photo" role="img" aria-label="Instructor leading a stretching class" style="left:342px;top:515px;width:153px;height:184px;background:linear-gradient(150deg,#e9e6e3,#c5beb8 55%,#4a4443)"></div>
  <div class="photo" role="img" aria-label="Coach taking notes beside a client in a studio" style="left:295px;top:552px;width:90px;height:129px;background:linear-gradient(160deg,#dcd8d4,#8c8682 60%,#3c3838);border:2px solid #fff"></div>

  <!-- services -->
  <p class="eyebrow" style="left:76px;top:726px">Make A New Start With The New You</p>
  <h2 class="h2" style="left:76px;top:741px">Services from <b>Novafit</b></h2>
  <p class="body" style="left:76px;top:763px;width:205px">Curabitur tincidunt velit quam, eu condimentum ligula bibendum ac. Duis volutpat mauris eu lacinia lobortis. Nulla facilisi. In accumsan sed massa sit amet pellentesque.</p>

  <div class="studio" role="img" aria-label="Athlete doing a bent-over exercise, tinted red"></div>
  <h3 style="left:86px;top:800px;font-family:'Sora',sans-serif;font-weight:700;font-size:27px;line-height:34px;color:#fff">Studio</h3>
  <div style="left:86px;top:837px;width:14px;height:1px;background:#fff"></div>
  <p class="body" style="left:86px;top:842px;width:150px;color:#f3dfe1">Curabitur tincidunt velit quam, eu condimentum ligula bibendum ac. Duis volutpat mauris eu lacinia lobortis. Nulla facilisi. In accumsan sed massa</p>
  <div class="pill" style="left:86px;top:862px;width:44px;height:9px;background:#f2ecea;color:var(--ink);font-size:4px">Know More &nbsp;→</div>

  <div class="services">Studio classes<br>Personal Training<br>Live Classes<br>Diet Coaching<br>In-Person Workouts<br>Remote Coaching</div>
  <div class="clip"><div class="services">Studio classes<br>Personal Training<br>Live Classes<br>Diet Coaching<br>In-Person Workouts<br>Remote Coaching</div></div>

  <div class="card" style="left:76px"><svg width="20" height="20" viewBox="0 0 20 20"><rect x="2" y="3" width="16" height="11" fill="none" stroke="#333" stroke-width="1"/><line x1="1" y1="17" x2="19" y2="17" stroke="#333"/></svg><p>Lorem ipsum dolor sit amet, consectetur adipiscing elit.</p></div>
  <div class="card" style="left:148px"><svg width="20" height="20" viewBox="0 0 20 20"><rect x="7" y="2" width="11" height="14" fill="none" stroke="#333"/><circle cx="5" cy="13" r="3" fill="none" stroke="#333"/></svg><p>Lorem ipsum dolor sit amet, consectetur adipiscing elit.</p></div>
  <div class="card" style="left:219px"><svg width="20" height="20" viewBox="0 0 20 20"><rect x="3" y="4" width="14" height="10" fill="none" stroke="#333"/><circle cx="10" cy="9" r="2.5" fill="none" stroke="#333"/><line x1="1" y1="17" x2="19" y2="17" stroke="#333"/></svg><p>Lorem ipsum dolor sit amet, consectetur adipiscing elit.</p></div>
  <div class="card" style="left:290px"><svg width="20" height="20" viewBox="0 0 20 20"><rect x="3" y="2" width="11" height="16" fill="none" stroke="#333"/><line x1="5" y1="7" x2="12" y2="7" stroke="#333"/><line x1="5" y1="11" x2="12" y2="11" stroke="#333"/><circle cx="16" cy="15" r="3" fill="none" stroke="#333"/></svg><p>Lorem ipsum dolor sit amet, consectetur adipiscing elit.</p></div>
  <div class="card" style="left:361px"><svg width="20" height="20" viewBox="0 0 20 20"><line x1="2" y1="6" x2="18" y2="6" stroke="#333"/><rect x="1" y="3" width="3" height="6" fill="none" stroke="#333"/><rect x="16" y="3" width="3" height="6" fill="none" stroke="#333"/><circle cx="10" cy="10" r="2" fill="none" stroke="#333"/><line x1="10" y1="12" x2="10" y2="18" stroke="#333"/></svg><p>Lorem ipsum dolor sit amet, consectetur adipiscing elit.</p></div>
  <div class="card" style="left:433px"><svg width="20" height="20" viewBox="0 0 20 20"><rect x="2" y="3" width="16" height="14" fill="none" stroke="#333"/><circle cx="7" cy="9" r="2.5" fill="none" stroke="#333"/><line x1="12" y1="7" x2="16" y2="7" stroke="#333"/><line x1="12" y1="11" x2="16" y2="11" stroke="#333"/></svg><p>Lorem ipsum dolor sit amet, consectetur adipiscing elit.</p></div>

  <!-- press -->
  <p style="left:76px;top:1232px;font-family:'Sora',sans-serif;font-weight:700;font-size:10px;line-height:13px"><span class="accent">Check</span><br>us on</p>
  <span class="arrow" style="left:121px;top:1239px;color:var(--ink)">⟵</span>
  <div class="press"><span>Vellum</span><span>Fortwell</span><span>The Sentinel</span><span>Marlowe</span></div>
  <span class="arrow" style="left:468px;top:1239px;color:var(--ink)">⟶</span>

  <!-- testimonials -->
  <div class="quote fade" style="left:0;width:138px"></div>
  <p class="qname" style="left:5px;top:1302px;opacity:.5">Lena Ortiz</p>
  <p class="body" style="left:5px;top:1328px;width:128px;opacity:.4">Lorem ipsum dolor sit amet, consectetur adipiscing elit, sed do eiusmod tempor incididunt ut labore et dolore magna aliqua.</p>
  <span class="arrow" style="left:160px;top:1327px">←</span>
  <div class="quote" style="left:183px;width:205px"></div>
  <div class="avatar" role="img" aria-label="Portrait of Theo Marsh" style="left:190px;top:1309px"></div>
  <p class="qname" style="left:255px;top:1302px">Theo Marsh</p>
  <p class="qrole" style="left:255px;top:1311px">Marketing Manager, Northgate</p>
  <p class="stars" style="left:255px;top:1318px">★★★★★</p>
  <p class="body" style="left:255px;top:1328px;width:128px">Lorem ipsum dolor sit amet, consectetur adipiscing elit, sed do eiusmod tempor incididunt ut labore et dolore magna aliqua. Quis ipsum suspendisse ultrices gravida. Risus commodo viverra maecenas accumsan lacus vel facilisis.</p>
  <span class="arrow" style="left:397px;top:1327px">→</span>
  <div class="quote fade" style="left:433px;width:138px"></div>
  <div class="avatar" role="img" aria-label="Portrait of Priya Vale" style="left:439px;top:1309px;opacity:.5"></div>
  <p class="qname" style="left:504px;top:1302px;opacity:.5">Priya Vale</p>

  <!-- subscribe -->
  <div class="frame" style="left:76px;top:1423px;width:60px;height:110px;border-right:none"></div>
  <div class="frame" style="left:168px;top:1440px;width:112px;height:119px;border-left:none;border-top:none"></div>
  <div class="photo" role="img" aria-label="Coach kneeling beside a client writing notes" style="left:82px;top:1411px;width:195px;height:141px;background:linear-gradient(140deg,#5c5757,#c8c4c0 55%,#ece9e6)"></div>
  <p class="eyebrow" style="left:325px;top:1430px">Change Your Life With Us</p>
  <h2 class="h2" style="left:325px;top:1445px;font-size:10px;line-height:13px"><b>Get</b> Latest News And Updates<br><b>subscribe</b> now</h2>
  <div style="left:325px;top:1482px;width:170px;height:22px;border-radius:12px;background:#f1eeec"></div>
  <p style="left:335px;top:1489px;font-size:5px;font-weight:500">Enter Your Email Address</p>
  <div class="pill" style="left:440px;top:1482px;width:55px;height:22px;border-radius:12px">Subscribe Now</div>
  <p class="body" style="left:325px;top:1514px;width:170px;color:var(--ink)">By entering email and subscribe you get the following notification and other details Lorem ipsum dolor sit amet, consectetur adipiscing elit, sed do eiusmod tempor incididunt ut labore et dolore magna aliqua.</p>

  <!-- footer -->
  <footer class="footer"></footer>
  <div class="logo" style="left:75px;top:1636px;font-size:20px">NOVAFIT</div>
  <div class="social" style="left:77px;top:1658px"></div>
  <div class="social" style="left:92px;top:1658px"></div>
  <div class="social" style="left:107px;top:1658px"></div>
  <div class="social" style="left:122px;top:1658px"></div>
  <div class="social" style="left:137px;top:1658px"></div>
  <div class="payc" style="left:77px"></div><div class="payc" style="left:93px"></div><div class="payc" style="left:109px"></div><div class="payc" style="left:125px"></div><div class="payc" style="left:141px"></div><div class="payc" style="left:157px"></div>
  <p class="fhead" style="left:219px;top:1620px">QUICK LINKS</p>
  <div class="flist" style="left:219px;top:1634px"><span>About</span><span>Services</span><span>The Journal</span><span>Blog</span><span>Shop</span></div>
  <div class="flist" style="left:255px;top:1634px"><span>Contact</span><span>Faq</span><span>Member</span><span>Signup</span><span>Sitemap</span></div>
  <p class="fhead" style="left:326px;top:1620px">CONNECT WITH US</p>
  <div class="flist" style="left:326px;top:1634px"><span>hello@novafit.example</span><span>care@novafit.example</span><span style="height:4px"></span><span>✆ 0555 014 220</span><span>✆ 0555 019 384</span><span>▪ 18 Elm Row, Harlow, State, Pin - 10293</span></div>
  <p class="fhead" style="left:433px;top:1620px">OTHER LINKS</p>
  <div class="flist" style="left:433px;top:1634px"><span>Search</span><span>Privacy Policy</span><span>Terms of Service</span><span>Members</span></div>
  <p style="right:77px;top:1686px;font-size:4.2px">Copyright © 2023, <span class="accent">Novafit</span> All rights reserved.</p>
</main>
</body>
</html>
```